Project Planning & Communication Process

Need a PowerPoint slide that illustrates our project planning and communication cycle. Our company has key meetings, and key communication vehicles (like emails and follow up tools) that we use to ensure our frontline staff are prepared to execute the new project successfully. This document needs to call out how the different components, like the meetings and emails, work together (like a flow chart), so someone who needs to use this process will understand what they should do. The slide needs to be simple yet comprehensive enough to guide someone through the details. I don't want it overwhelming. The primary focus is the process, not the details.

Use the color pallette included within the slide (shades of blue and gray, and black). This is for an insurance company (www.marrowpine.com). Use this as a reference for the look and feel.

I have attached a sample slide of the flow chart process.

Click here if you cannot access the file. https://www.stashloft.com/s/qx7rmt2pbn9wkaz/Communcation_Methods_V1.pptx

If you are not able to see the uploaded slide.  Please send me your email address and I will send the slide to you directly. 

ISince I'm not able to upload the reference ppt file, 've uploaded the slide at StashLoft.  Please click here to access.
https://www.stashloft.com/s/qx7rmt2pbn9wkaz/Communcation_Methods_V1.pptx

Reason: extending one more day for designers to make last minute updates.

Target Market(s)

Vice Presidents and project managers/business partners within the organization.

Industry/Entity Type

Communication

Font styles to use
Sans Serif

Colors
3176b5

Requirements
Must have
• 1 page, color pallette assigned, be simple yet comprehensive. the focus needs to be on the process, not on the details.
Nice to have
• Doesn't have to follow the example I provided. Please feel free to approach from different ways.

```html
<!DOCTYPE html>
<html lang="en">
<head>
<meta charset="utf-8">
<title>Project Alignment &amp; Communication Process</title>
<link href="https://fonts.googleapis.com/css2?family=Roboto:wght@300;400;700&display=swap" rel="stylesheet">
<style>
  :root {
    --white: #ffffff;
    --title-blue: #22a9e6;
    --brand-blue: #2a78bf;
    --band-planning: #5574bf;
    --band-prepare: #1f91c3;
    --band-follow: #0eafe9;
    --body-light: #e1e3e4;
    --body-mid: #c0bfc0;
    --body-dark: #808184;
    --icon-deep: #2f72b3;
    --icon-bright: #10abeb;
    --icon-teal: #1d8bbf;
    --overview: #b6d4ef;
    --purpose: #7cc1ea;
    --overview-cyan: #9ed9f5;
    --purpose-cyan: #abdee8;
    --digest: #9dd9f6;
    --follow-box: #b8e4f8;
    --wave: #1b8fd0;
    --text-gray: #6d6e70;
    --label-white: #f4f6f8;
  }
  * { margin: 0; padding: 0; box-sizing: border-box; }
  html, body { width: 1200px; height: 902px; overflow: hidden; background: var(--white); }
  body { font-family: "Roboto", "Helvetica Neue", Arial, sans-serif; font-weight: 300; }
  .slide { position: relative; width: 1200px; height: 902px; overflow: hidden; background: var(--white); }

  .slide-title { position: absolute; left: 54px; top: 44px; font-size: 29px; font-weight: 300; color: var(--title-blue); letter-spacing: 0.2px; }
  .header-divider { position: absolute; left: 734px; top: 38px; width: 2px; height: 64px; background: var(--title-blue); }
  .brand { position: absolute; left: 818px; top: 42px; display: flex; align-items: center; gap: 12px; }
  .brand-name { font-size: 32px; font-weight: 400; color: var(--brand-blue); }
  .brand-mark { width: 26px; height: 26px; border-radius: 50%; background: var(--brand-blue); }

  .phase { position: absolute; top: 133px; height: 78px; color: var(--white); font-size: 24px; font-weight: 300; display: flex; align-items: center; justify-content: center; }
  .phase-planning { left: 0; width: 717px; background: var(--band-planning); }
  .phase-prepare { left: 717px; width: 334px; background: var(--band-prepare); }
  .phase-follow { left: 1051px; width: 149px; background: var(--band-follow); font-size: 21px; line-height: 18px; justify-content: flex-start; padding-left: 9px; }

  .zone { position: absolute; top: 211px; height: 691px; }
  .zone-planning { left: 0; width: 717px; background: var(--body-light); }
  .zone-prepare { left: 717px; width: 334px; background: var(--body-mid); }
  .zone-follow { left: 1051px; width: 149px; background: var(--body-dark); }

  .step { position: absolute; top: 268px; width: 110px; margin-left: -55px; text-align: center; }
  .step-icon { display: block; margin: 0 auto; width: 74px; height: 74px; }
  .step-label { margin-top: 16px; font-size: 17px; line-height: 20px; color: var(--text-gray); }
  .step-label.on-dark { color: var(--label-white); }

  .card { position: absolute; font-size: 13px; line-height: 16px; color: var(--text-gray); }
  .card strong { font-weight: 700; display: block; }
  .card-col { position: absolute; top: 20px; width: 100px; }

  .overview-go { left: 141px; top: 458px; width: 128px; height: 202px; background: var(--overview); }
  .purpose-go { left: 141px; top: 660px; width: 128px; height: 130px; background: var(--purpose); }
  .overview-milestones { left: 377px; top: 458px; width: 340px; height: 200px; background: var(--overview); }
  .purpose-milestones { left: 377px; top: 658px; width: 340px; height: 132px; background: var(--purpose); }
  .overview-center { left: 717px; top: 458px; width: 128px; height: 200px; background: var(--overview-cyan); }
  .purpose-center { left: 717px; top: 658px; width: 128px; height: 160px; background: var(--purpose-cyan); }
  .digest-note { left: 935px; top: 458px; width: 116px; height: 420px; background: var(--digest); }
  .followup-note { left: 1051px; top: 458px; width: 149px; height: 420px; background: var(--follow-box); }

  .wave { position: absolute; left: 0; top: 700px; width: 1200px; height: 202px; }
</style>
</head>
<body>
<div class="slide">
  <h1 class="slide-title">Project Alignment &amp; Communication Process</h1>
  <div class="header-divider"></div>
  <div class="brand"><span class="brand-name">Marrowpine</span><span class="brand-mark"></span></div>

  <div class="phase phase-planning">Planning &amp; Design Phase</div>
  <div class="phase phase-prepare">Prepare Phase</div>
  <div class="phase phase-follow">Follow up &amp;<br>Evaluate</div>

  <div class="zone zone-planning"></div>
  <div class="zone zone-prepare"></div>
  <div class="zone zone-follow"></div>

  <!-- Steps -->
  <div class="step" style="left:104px">
    <svg class="step-icon" viewBox="0 0 74 74"><circle cx="37" cy="37" r="37" fill="var(--icon-deep)"/><circle cx="37" cy="32" r="11" fill="#fff"/><rect x="32" y="40" width="10" height="9" fill="#fff"/><g stroke="#fff" stroke-width="1.5"><line x1="21" y1="32" x2="17" y2="32"/><line x1="53" y1="32" x2="57" y2="32"/><line x1="24" y1="44" x2="21" y2="47"/><line x1="50" y1="44" x2="53" y2="47"/></g></svg>
    <div class="step-label">New Prcject Identified</div>
  </div>
  <div class="step" style="left:215px">
    <svg class="step-icon" viewBox="0 0 74 74"><circle cx="37" cy="37" r="37" fill="var(--icon-bright)"/><g fill="#fff"><circle cx="37" cy="27" r="6"/><path d="M27 46a10 10 0 0 1 20 0z"/><circle cx="24" cy="31" r="5"/><path d="M16 46a8 8 0 0 1 16 0z"/><circle cx="50" cy="31" r="5"/><path d="M42 46a8 8 0 0 1 16 0z"/></g></svg>
    <div class="step-label">Governance Meeting</div>
  </div>
  <div class="step" style="left:326px">
    <svg class="step-icon" viewBox="0 0 74 74"><circle cx="37" cy="37" r="37" fill="var(--icon-deep)"/><path d="M20 26h12l3 4h19v20H20z" fill="#fff"/><path d="M20 50l5-16h34l-5 16z" fill="#e6eef6"/></svg>
    <div class="step-label">Separate Project Meetings as needed</div>
  </div>
  <div class="step" style="left:437px">
    <svg class="step-icon" viewBox="0 0 74 74"><circle cx="37" cy="37" r="37" fill="var(--icon-bright)"/><g fill="#fff"><circle cx="37" cy="27" r="6"/><path d="M27 46a10 10 0 0 1 20 0z"/><circle cx="24" cy="31" r="5"/><path d="M16 46a8 8 0 0 1 16 0z"/><circle cx="50" cy="31" r="5"/><path d="M42 46a8 8 0 0 1 16 0z"/></g></svg>
    <div class="step-label" style="margin-top:21px">Governance Meeting</div>
  </div>
  <div class="step" style="left:550px">
    <svg class="step-icon" viewBox="0 0 74 74"><circle cx="37" cy="37" r="37" fill="var(--icon-bright)"/><g fill="#fff"><circle cx="37" cy="27" r="6"/><path d="M27 46a10 10 0 0 1 20 0z"/><circle cx="24" cy="31" r="5"/><path d="M16 46a8 8 0 0 1 16 0z"/><circle cx="50" cy="31" r="5"/><path d="M42 46a8 8 0 0 1 16 0z"/></g></svg>
    <div class="step-label" style="margin-top:19px">Weekly Center Leader Meeting</div>
  </div>
  <div class="step" style="left:660px">
    <svg class="step-icon" viewBox="0 0 74 74"><circle cx="37" cy="37" r="37" fill="var(--icon-bright)"/><g fill="#fff"><circle cx="37" cy="27" r="6"/><path d="M27 46a10 10 0 0 1 20 0z"/><circle cx="24" cy="31" r="5"/><path d="M16 46a8 8 0 0 1 16 0z"/><circle cx="50" cy="31" r="5"/><path d="M42 46a8 8 0 0 1 16 0z"/></g></svg>
    <div class="step-label">Field Advisory Panel</div>
  </div>
  <div class="step" style="left:771px">
    <svg class="step-icon" viewBox="0 0 74 74"><circle cx="37" cy="37" r="37" fill="var(--icon-bright)"/><g fill="#fff"><circle cx="37" cy="27" r="6"/><path d="M27 46a10 10 0 0 1 20 0z"/><circle cx="24" cy="31" r="5"/><path d="M16 46a8 8 0 0 1 16 0z"/><circle cx="50" cy="31" r="5"/><path d="M42 46a8 8 0 0 1 16 0z"/></g></svg>
    <div class="step-label">Weekly Center Leader Meeting</div>
  </div>
  <div class="step" style="left:882px">
    <svg class="step-icon" viewBox="0 0 74 74"><circle cx="37" cy="37" r="37" fill="var(--icon-teal)"/><path d="M26 22h16l7 7v23H26z" fill="#fff"/></svg>
    <div class="step-label">Monday Memo</div>
  </div>
  <div class="step" style="left:994px">
    <svg class="step-icon" viewBox="0 0 74 74"><circle cx="37" cy="37" r="37" fill="var(--icon-teal)"/><rect x="21" y="20" width="32" height="33" rx="3" fill="#fff"/><rect x="24" y="29" width="26" height="21" fill="var(--icon-teal)"/><rect x="25" y="30" width="24" height="19" fill="#fff"/><text x="37" y="27" font-size="5" font-weight="700" text-anchor="middle" fill="var(--icon-teal)" font-family="Roboto, sans-serif">JANUARY</text><text x="37" y="46" font-size="14" font-weight="700" text-anchor="middle" fill="#333" font-family="Roboto, sans-serif">01</text></svg>
    <div class="step-label" style="margin-top:18px">Daily Digest</div>
  </div>
  <div class="step" style="left:1104px">
    <svg class="step-icon" viewBox="0 0 74 74"><circle cx="37" cy="37" r="37" fill="var(--icon-teal)"/><rect x="24" y="24" width="26" height="26" rx="4" fill="none" stroke="#fff" stroke-width="4"/><path d="M29 37l6 6 14-15" fill="none" stroke="#fff" stroke-width="4"/></svg>
    <div class="step-label on-dark">Follow Up Guide</div>
  </div>

  <!-- Detail cards -->
  <div class="card overview-go"><div class="card-col" style="left:23px;top:20px"><strong>Overview:</strong>Project Owner presents one pager to Sr Leadership. Based on Business Value, and Capacity a Go/No Go Decision is made.</div></div>
  <div class="card purpose-go"><div class="card-col" style="left:23px;top:10px"><strong>Purpose:</strong>Go/No Go Decision</div></div>

  <div class="card overview-milestones">
    <div class="card-col" style="left:24px"><strong>Overview:</strong>Project Owner presents milestones and feedback/app rovals during key decision points.</div>
    <div class="card-col" style="left:135px"><strong>Overview:</strong>Project Owner presents project and collect Center Staff Feedback</div>
    <div class="card-col" style="left:243px;width:90px"><strong>Overview:</strong>Project Owner presents milestones and feedback/app rovals during key decision points.</div>
  </div>
  <div class="card purpose-milestones">
    <div class="card-col" style="left:24px;top:12px"><strong>Purpose:</strong>Report out on Milestone status and Key Decision Points</div>
    <div class="card-col" style="left:135px;top:12px"><strong>Purpose:</strong>Collect Center Staff Feedback</div>
    <div class="card-col" style="left:243px;top:12px;width:94px"><strong>Purpose:</strong>Report out on Milestone status and Key Decision Points</div>
  </div>

  <div class="card overview-center"><div class="card-col" style="left:17px"><strong>Overview:</strong>Project Owner presents project and implemen-tation details to ensure Center Leaders are prepared.</div></div>
  <div class="card purpose-center"><div class="card-col" style="left:17px;top:12px"><strong>Purpose:</strong>Center Planning and Specific execution details.<br>WHEN: 1 month out</div></div>

  <div class="card digest-note"><div class="card-col" style="left:21px"><span>Just in Time Notice / Follow up for execution.</span></div></div>
  <div class="card followup-note"><div class="card-col" style="left:17px"><span>Post Launch</span></div></div>

  <svg class="wave" viewBox="0 0 1200 202" preserveAspectRatio="none" aria-hidden="true">
    <path d="M0 90 C 200 60, 600 60, 800 100 C 880 118, 930 140, 955 158 C 1020 90, 1100 40, 1200 32 L1200 202 L0 202 Z" fill="var(--wave)"/>
  </svg>
</div>
</body>
</html>
```